Building company buisness cards

We are looking for a sharp modern new look for our business cards.
We are a New Zealand based company that specialises in house and land packages.
We have attached a photo of the current logo and would like to see if it can be improved somehow if needed.
We are open to any colours but we have chosen green at this stage.
Feel free to change the font and make the logo smarter looking.
Play with the colours and see what looks best.

We want a card that looks so good know one will want to throw it away!

Target Market(s)

Home buyers

Industry/Entity Type

Building

Contact Information for Business Card

Dorian Keswick
0217392604
dkeswick@tidewellhomecraft.co.nz
tidewellhomecraft.co.nz

Font styles to use
Serif
Sans Serif

Colors

Designer to choose colors to be used in the design.

Requirements
Must have
• Logo and company name on one side, details on the other side
Nice to have
• Color codes for the original green are HEX #4a8028, RGB(74,128,40), CMYK(42,0,69,50)
• Round corners, Raised and/or spot UV

```html
<!DOCTYPE html>
<html lang="en">
<head>
<meta charset="utf-8">
<title>Tidewell Homecraft business cards</title>
<link rel="stylesheet" href="https://fonts.googleapis.com/css2?family=Montserrat:wght@500&family=Nunito:wght@900&display=swap">
<style>
  :root {
    --bg: #1d1d1d;
    --green: #4a8028;
    --green-fold: rgba(0, 0, 0, 0.16);
    --green-light: rgba(255, 255, 255, 0.07);
    --ink: #ffffff;
  }
  * { margin: 0; padding: 0; box-sizing: border-box; }
  html, body {
    width: 1200px; height: 900px; overflow: hidden;
    background: var(--bg);
  }
  .stage { position: relative; width: 1200px; height: 900px; }

  .card {
    position: absolute;
    width: 520px; height: 297px;
    background: var(--green);
    border-radius: 6px;
    overflow: hidden;
    box-shadow: 0 10px 30px rgba(0,0,0,0.5);
    color: var(--ink);
  }
  .card--details { left: 70px; top: 130px; }
  .card--brand { left: 610px; top: 470px; }

  /* raised panel lines */
  .fold { position: absolute; }
  .fold--h { left: 0; right: 0; height: 0;
    border-top: 1px solid var(--green-fold);
    box-shadow: 0 -6px 10px var(--green-fold), 0 1px 0 var(--green-light); }
  .fold--v { top: 0; bottom: 0; width: 0;
    border-left: 1px solid var(--green-fold);
    box-shadow: -6px 0 10px var(--green-fold), 1px 0 0 var(--green-light); }

  .company-name {
    font-family: "Montserrat", sans-serif;
    font-weight: 500;
    color: var(--ink);
    white-space: nowrap;
    display: flex; align-items: center; gap: 10px;
  }
  .company-name__mark {
    width: 12px; height: 12px; border-radius: 50%;
    background: var(--ink); flex: none;
  }

  .card--details .company-name { position: absolute; left: 26px; top: 36px; font-size: 16px; }
  .holder-name {
    position: absolute; right: 26px; top: 30px;
    font-family: "Nunito", sans-serif; font-weight: 900;
    font-size: 27px; letter-spacing: -0.2px;
  }

  .contact-list { position: absolute; left: 86px; top: 118px; list-style: none; }
  .contact-item {
    display: flex; align-items: center; gap: 16px;
    height: 46px;
    font-family: "Montserrat", sans-serif; font-weight: 500;
    font-size: 16px;
  }
  .contact-icon { width: 18px; height: 18px; flex: none; }

  .card--brand .company-name {
    position: absolute; left: 0; right: 0; top: 132px;
    justify-content: center; font-size: 28px;
  }
</style>
</head>
<body>
<main class="stage">

  <section class="card card--details" aria-label="Details side">
    <div class="fold fold--h" style="top:88px"></div>
    <div class="fold fold--v" style="left:34px; top:88px"></div>
    <div class="fold fold--v" style="left:66px; top:88px"></div>

    <div class="company-name">
      <span class="company-name__mark"></span>
      <span>Tidewell Homecraft</span>
    </div>
    <h1 class="holder-name">Dorian Keswick</h1>

    <ul class="contact-list">
      <li class="contact-item">
        <svg class="contact-icon" viewBox="0 0 24 24" aria-hidden="true"><path fill="#fff" d="M6.6 10.8a15 15 0 0 0 6.6 6.6l2.2-2.2c.3-.3.7-.4 1-.2 1.1.4 2.3.6 3.6.6.6 0 1 .4 1 1V20c0 .6-.4 1-1 1A17 17 0 0 1 3 4c0-.6.4-1 1-1h3.5c.6 0 1 .4 1 1 0 1.3.2 2.5.6 3.6.1.3 0 .7-.2 1z"/></svg>
        <span>0217392604</span>
      </li>
      <li class="contact-item">
        <svg class="contact-icon" viewBox="0 0 24 24" aria-hidden="true"><rect x="2" y="5" width="20" height="14" fill="#fff"/><path d="M2 5l10 8 10-8M2 19l7-7M22 19l-7-7" stroke="#4a8028" stroke-width="1.6" fill="none"/></svg>
        <span>dkeswick@tidewellhomecraft.co.nz</span>
      </li>
      <li class="contact-item">
        <svg class="contact-icon" viewBox="0 0 24 24" aria-hidden="true" fill="none" stroke="#fff" stroke-width="1.4"><circle cx="12" cy="12" r="9.5"/><ellipse cx="12" cy="12" rx="4.5" ry="9.5"/><path d="M2.5 12h19M4 7h16M4 17h16M12 2.5v19"/></svg>
        <span>tidewellhomecraft.co.nz</span>
      </li>
    </ul>
  </section>

  <section class="card card--brand" aria-label="Brand side">
    <div class="fold fold--h" style="top:66px"></div>
    <div class="fold fold--h" style="top:232px"></div>
    <div class="fold fold--v" style="left:78px"></div>
    <div class="fold fold--v" style="left:442px"></div>

    <div class="company-name">
      <span class="company-name__mark" style="width:16px;height:16px"></span>
      <span>Tidewell Homecraft</span>
    </div>
  </section>

</main>
</body>
</html>
```